TRELBY Construction Group business card for distribution

A business card detailing our services, with our phone number and email address.
- Groundworks / Foundations / Drainage
- Landscaping / Hard Landscaping / Patios / Decking
- Fencing
The card should include company logo and be in the same colours.

Target Market(s)
Domestic Houses
Industry/Entity Type
Construction
Contact Information for Business Card
Phone Number - 07731 248 905 / 07612093184. Email address: trelbygroup@fenwickmail.com
Font styles to use
Serif
Sans Serif
Colors
F0912C
F2A743
F7CA91
FBE8D2
FDF5EE
Requirements
Must have
- Contact numbers. Photos of past work. Company Logo

Nice to have
- Company Logo

```html
<!DOCTYPE html>
<html lang="en">
<head>
<meta charset="utf-8">
<title>TRELBY Construction Group – Business Card</title>
<link rel="stylesheet" href="https://fonts.googleapis.com/css2?family=Montserrat:wght@400;500;600;700;800&display=swap">
<style>
  :root {
    --orange: #f0912c;
    --orange-soft: #f2a743;
    --ink: #231f20;
    --text: #2b2b2b;
    --card: #ffffff;
    --backdrop: #e9e7e4;
  }
  * { box-sizing: border-box; margin: 0; padding: 0; }
  html, body {
    width: 1200px; height: 913px; overflow: hidden;
    background: var(--backdrop);
    font-family: "Montserrat", Arial, sans-serif;
    color: var(--text);
  }
  .canvas { position: relative; width: 1200px; height: 913px; }

  .card {
    position: absolute;
    width: 560px; height: 320px;
    background: var(--card);
    border-radius: 22px;
    border-bottom: 5px solid var(--orange);
    box-shadow: 0 10px 24px rgba(0,0,0,.12);
    overflow: hidden;
  }
  .card--front { left: 90px; top: 100px; }
  .card--back  { left: 550px; top: 490px; }

  /* brand mark */
  .brand { display: flex; align-items: center; gap: 12px; }
  .brand__square { width: 22px; height: 22px; background: var(--orange); flex: none; }
  .brand__name {
    font-weight: 700; color: var(--ink);
    letter-spacing: .05em; text-transform: uppercase; line-height: 1.2;
  }

  /* front */
  .card--front .brand { position: absolute; left: 80px; right: 60px; top: 70px; }
  .card--front .brand__name { font-size: 27px; }
  .services { position: absolute; left: 24px; right: 24px; top: 180px; text-align: center; }
  .services__title {
    color: var(--orange); font-weight: 700; font-size: 15px;
    letter-spacing: .03em; margin-bottom: 8px;
  }
  .services__line { font-size: 15px; font-weight: 500; line-height: 1.55; }
  .services__line--wide { font-size: 14px; }
  .dot {
    display: inline-block; width: 10px; height: 10px; border-radius: 50%;
    background: var(--orange); margin: 0 6px 1px; vertical-align: middle;
  }

  /* back */
  .card--back .brand { position: absolute; left: 36px; top: 150px; width: 220px; }
  .card--back .brand__name { font-size: 17px; }
  .divider {
    position: absolute; left: 272px; top: 40px; width: 2px; height: 220px;
    background: var(--orange);
  }
  .contact { position: absolute; left: 294px; right: 28px; top: 62px; }
  .contact__name {
    color: var(--orange); font-weight: 800; font-size: 22px;
    letter-spacing: .02em; text-transform: uppercase; line-height: 1.1;
    white-space: nowrap;
  }
  .contact__role { font-size: 14px; font-weight: 500; margin: 6px 0 20px; }
  .contact__row {
    display: flex; align-items: center; gap: 9px;
    font-size: 14px; font-weight: 500; line-height: 1; margin-bottom: 10px;
    white-space: nowrap;
  }
  .contact__row svg { width: 14px; height: 14px; flex: none; fill: var(--orange); }
  .contact__row--email { font-size: 12.5px; }
</style>
</head>
<body>
<main class="canvas">

  <section class="card card--front" aria-label="Card front">
    <div class="brand">
      <span class="brand__square"></span>
      <span class="brand__name">TRELBY Construction Group Ltd</span>
    </div>
    <div class="services">
      <p class="services__title">OUR SERVICES</p>
      <p class="services__line">Groundworks / Foundations / Drainage</p>
      <p class="services__line services__line--wide">
        <span class="dot"></span>Landscaping / Hard Landscaping / Patios / Decking<span class="dot"></span>Fencing
      </p>
    </div>
  </section>

  <section class="card card--back" aria-label="Card back">
    <div class="brand">
      <span class="brand__square"></span>
      <span class="brand__name">TRELBY<br>Construction Group Ltd</span>
    </div>
    <span class="divider"></span>
    <div class="contact">
      <p class="contact__name">Daniel Orwell</p>
      <p class="contact__role">Managing Director</p>
      <p class="contact__row">
        <svg viewBox="0 0 24 24" aria-hidden="true"><path d="M3 9c0-3 4-5 9-5s9 2 9 5v2h-5V9c-1-.6-2.5-1-4-1s-3 .4-4 1v2H3z M6 12h12l2 8H4z"/></svg>
        07731 248 905
      </p>
      <p class="contact__row">
        <svg viewBox="0 0 24 24" aria-hidden="true"><path d="M3 9c0-3 4-5 9-5s9 2 9 5v2h-5V9c-1-.6-2.5-1-4-1s-3 .4-4 1v2H3z M6 12h12l2 8H4z"/></svg>
        07612093184
      </p>
      <p class="contact__row contact__row--email">
        <svg viewBox="0 0 24 24" aria-hidden="true"><path d="M2 5h20v14H2z" fill="none" stroke="#f0912c" stroke-width="2.5"/><path d="M2 6l10 7 10-7" fill="none" stroke="#f0912c" stroke-width="2.5"/></svg>
        trelbygroup@fenwickmail.com
      </p>
    </div>
  </section>

</main>
</body>
</html>
```